Best in class cloud software provider for retailers needs a new business card design to reflect prod

We are a software company based out of Chicago selling into retailers. We have a new website and marketing collateral that support our new product designs. We are obsessed with simplicity, ease of use, and having a really powerful product set. We have two products as noted on our website - www.brolvane.com - one is a retail task management product and the other is a Help Ticketing product.

At Brolvane we are passionate about creating the best Retail Task Management system in the industry. We bring more than 20 years of retail operations, Workforce Management and Retail Task experience and have a set of web and mobile software features that no one else has. Brolvane enables you to plan and distribute work throughout your organization and ensure it gets done.

We need a new business card design that reflects our new branding, message and approach.

I've attached a few documents that help support what we are building and how our colors look.

There may be additional future work if this goes well.

Thanks,
Mark

President

Target Market(s)

We sell into retailers and are a software company

Industry/Entity Type

Software

Contact Information for Business Card

The card must have

Name
title
address
tele
email
Brolvane logo (someplace)

So for example

It would have for me

Mark Dorsett
President
48 West Harlow Ave. Suite 310
Chicago, IL 60687
3125550187
mdorsett@brolvane.com

Requirements
Must have
• We need to cards for 5 different people - same design different names etc
Nice to have
• should reflect our colors and product and website - be creative - ease of use, simplicity, and power is what the product is about - but we are very forward Brolvane and hear all the time that our product is gorgeous. The font should be consistent with our website, and marketing one pager included
Should not have
• Strange or unfamiliar colors or fonts...

```html
<!DOCTYPE html>
<html lang="en">
<head>
<meta charset="utf-8">
<title>Brolvane Business Card</title>
<link href="https://fonts.googleapis.com/css2?family=Open+Sans:wght@400;700&display=swap" rel="stylesheet">
<style>
  :root {
    --brand-blue: #2aa3c6;
    --brand-blue-deep: #1f83a8;
    --slate: #3d3e40;
    --paper: #f6f7f7;
    --ink: #444648;
    --stage: #e4e6e8;
  }
  * { box-sizing: border-box; margin: 0; padding: 0; }
  html, body { width: 1200px; height: 780px; overflow: hidden; }
  body {
    background: var(--stage);
    font-family: "Open Sans", sans-serif;
    position: relative;
  }
  .card {
    position: absolute;
    width: 560px;
    height: 320px;
    overflow: hidden;
    box-shadow: 0 6px 18px rgba(0,0,0,0.18);
  }
  /* Front */
  .card-front { left: 60px; top: 60px; background: var(--paper); }
  .front-brand-panel {
    position: absolute; left: 0; top: 0; width: 365px; height: 160px;
    background: linear-gradient(180deg, var(--brand-blue-deep), var(--brand-blue));
    display: flex; align-items: center; justify-content: center;
  }
  .wordmark {
    font-family: "Open Sans", sans-serif;
    font-weight: 700;
    letter-spacing: -1px;
  }
  .front-brand-panel .wordmark { color: #ffffff; font-size: 62px; }
  .front-contact-panel {
    position: absolute; left: 0; top: 160px; width: 365px; height: 160px;
    background: var(--paper);
    padding: 26px 0 0 70px;
  }
  .person-name { color: var(--brand-blue-deep); font-weight: 700; font-size: 25px; line-height: 1.1; }
  .person-title { color: var(--ink); font-size: 15px; margin-bottom: 12px; }
  .contact-list { list-style: none; }
  .contact-item { display: flex; align-items: center; gap: 8px; color: var(--ink); font-size: 14px; line-height: 21px; }
  .contact-icon { width: 15px; height: 15px; flex: none; }
  .front-address-panel {
    position: absolute; left: 365px; top: 0; width: 195px; height: 320px;
    background: var(--slate);
    padding: 0 0 24px 24px;
    display: flex; flex-direction: column; justify-content: flex-end;
  }
  .address { color: #e8e8e8; font-size: 13px; line-height: 19px; font-style: normal; }
  /* Back */
  .card-back {
    left: 580px; top: 400px;
    background: linear-gradient(180deg, var(--brand-blue-deep), var(--brand-blue) 50%, var(--brand-blue-deep));
  }
  .back-band {
    position: absolute; left: 0; top: 92px; width: 100%; height: 136px;
    background: var(--paper);
    display: flex; align-items: center; justify-content: center;
  }
  .back-rule { position: absolute; left: 0; width: 100%; height: 3px; background: var(--paper); }
  .back-rule.upper { top: 82px; }
  .back-rule.lower { top: 235px; }
  .back-band .wordmark { color: var(--brand-blue); font-size: 60px; }
</style>
</head>
<body>
  <section class="card card-front" aria-label="Business card front">
    <div class="front-brand-panel">
      <span class="wordmark">Brolvane</span>
    </div>
    <div class="front-contact-panel">
      <p class="person-name">Mark Dorsett</p>
      <p class="person-title">President</p>
      <ul class="contact-list">
        <li class="contact-item">
          <svg class="contact-icon" viewBox="0 0 16 16" aria-hidden="true"><rect width="16" height="16" rx="2" fill="#2aa3c6"/><path d="M5 3.5l2 2.2-1 1.3c.7 1.4 1.6 2.3 3 3l1.3-1 2.2 2-1 1.5c-3.6-.4-6.6-3.4-7-7z" fill="#fff"/></svg>
          <span>3125550187</span>
        </li>
        <li class="contact-item">
          <svg class="contact-icon" viewBox="0 0 16 16" aria-hidden="true"><rect width="16" height="16" rx="2" fill="#2aa3c6"/><rect x="3" y="4.5" width="10" height="7" fill="none" stroke="#fff" stroke-width="1.2"/><path d="M3 4.5l5 4 5-4" fill="none" stroke="#fff" stroke-width="1.2"/></svg>
          <span>mdorsett@brolvane.com</span>
        </li>
        <li class="contact-item">
          <svg class="contact-icon" viewBox="0 0 16 16" aria-hidden="true"><rect width="16" height="16" rx="2" fill="#2aa3c6"/><circle cx="8" cy="8" r="4.6" fill="none" stroke="#fff" stroke-width="1.1"/><ellipse cx="8" cy="8" rx="2" ry="4.6" fill="none" stroke="#fff" stroke-width="1"/><path d="M3.4 8h9.2" stroke="#fff" stroke-width="1"/></svg>
          <span>www.brolvane.com</span>
        </li>
      </ul>
    </div>
    <div class="front-address-panel">
      <address class="address">48 West Harlow Ave. Suite 310<br>Chicago, IL 60687</address>
    </div>
  </section>

  <section class="card card-back" aria-label="Business card back">
    <div class="back-rule upper"></div>
    <div class="back-band">
      <span class="wordmark">Brolvane</span>
    </div>
    <div class="back-rule lower"></div>
  </section>
</body>
</html>
```